Beef 100 % Cooked Ready to Eat in a Metal Can

Design a label for a Beef Product 100 % Pure ,Cooked and ready to eat , Be sold in Africa . The label to be in English and French , Or English and Portuguese . Need either a photo or a drawing showing a Bull or Cow .

BRAND Name of the product is " 100% TAURA
Plus + Picture of a Bull or Cow and after to expand Range to include 100 % Mutton , The label should be easy to reproduce and Art work in BALCK AND WHITE for point of sale POSTERS for Advertising . T Shirts ect
Updates

Check out the updated Brief ,and Maybe I will in crease the Budget !

Target Market(s)

African People , Children , illiterate ,Some of the target People who Can read and some can't , From Age 16 - 40 males and female

Image /drawing /or Photo of Bull Or Cow must be Prominent ,

The word 100 % BEEF . Most People can Understand even the ones that cat read

Background color should be stand out form Competitors

Industry/Entity Type

Advertising

Font styles to use
Sans Serif

Colors

Designer to choose colors to be used in the design.

Requirements
Must have

• Recognizable ,easy to remember , Symbols , Image +100%+ Beef = Good Label

Bright Colour ,
Nice to have
• Positive color

Simple Not too Much Copy .

Tin Will Have Ingredients in Small and Bar code in Small .
Should not have
• Modern look .as for Traditional ,Market ,

```html
<!DOCTYPE html>
<html lang="en">
<head>
<meta charset="UTF-8">
<title>100% Taura – Can Label</title>
<link rel="stylesheet" href="https://fonts.googleapis.com/css2?family=Josefin+Sans:wght@400;600&family=Roboto:wght@700&display=swap">
<style>
  :root {
    --backdrop-light: #e4e4e4;
    --backdrop-dark: #b9b9b9;
    --badge-orange: #f2a318;
    --badge-red: #c8231c;
    --badge-yellow-light: #fff3a6;
    --badge-yellow: #fbd650;
    --badge-yellow-deep: #f6b92a;
    --ribbon-red: #c4121a;
    --ribbon-dark: #7a0a0c;
    --ribbon-text: #ffd23a;
    --artwork-dark: #3a241b;
    --artwork-mid: #6b4a2c;
  }
  html, body {
    margin: 0;
    padding: 0;
    width: 1200px;
    height: 1000px;
    overflow: hidden;
  }
  body {
    background: radial-gradient(ellipse at 50% 45%, var(--backdrop-light) 0%, var(--backdrop-dark) 100%);
  }
  .label-canvas {
    position: relative;
    width: 1200px;
    height: 1000px;
  }
  .label-art {
    position: absolute;
    inset: 0;
  }
  .brand-title {
    font-family: "Josefin Sans", sans-serif;
    font-weight: 400;
    fill: var(--badge-red);
    text-anchor: middle;
  }
  .brand-percent { font-size: 96px; }
  .brand-word { font-size: 104px; letter-spacing: 4px; }
  .ribbon-text {
    font-family: "Roboto", sans-serif;
    font-weight: 700;
    fill: var(--ribbon-text);
  }
  .ribbon-text-main { font-size: 30px; letter-spacing: 1px; }
  .ribbon-text-sub { font-size: 25px; }
</style>
</head>
<body>
<main class="label-canvas">
  <svg class="label-art" width="1200" height="1000" viewBox="0 0 1200 1000" xmlns="http://www.w3.org/2000/svg">
    <defs>
      <linearGradient id="badgeFill" x1="0" y1="0" x2="0" y2="1">
        <stop offset="0" stop-color="var(--badge-yellow-light)"/>
        <stop offset="0.55" stop-color="var(--badge-yellow)"/>
        <stop offset="1" stop-color="var(--badge-yellow-deep)"/>
      </linearGradient>
      <linearGradient id="ribbonFill" x1="0" y1="0" x2="1" y2="0">
        <stop offset="0" stop-color="#9e0e12"/>
        <stop offset="0.4" stop-color="var(--ribbon-red)"/>
        <stop offset="1" stop-color="#a80f14"/>
      </linearGradient>
      <radialGradient id="artworkFill" cx="0.5" cy="0.45" r="0.65">
        <stop offset="0" stop-color="var(--artwork-mid)"/>
        <stop offset="1" stop-color="var(--artwork-dark)"/>
      </radialGradient>
      <path id="ribbonLineOne" d="M400,745 C520,830 690,830 820,745"/>
      <path id="ribbonLineTwo" d="M380,785 C510,875 700,875 840,780"/>
    </defs>

    <path class="ribbon-tail-left" d="M330,690 C300,640 330,610 380,600 L390,700 Z" fill="var(--ribbon-dark)"/>
    <path class="ribbon-tail-right" d="M860,760 C900,800 900,850 870,880 L820,870 L830,780 Z" fill="var(--ribbon-dark)"/>

    <path class="badge-outer" d="M375,250 Q405,250 405,215 Q600,110 795,215 Q795,250 825,250 L825,790 Q825,905 600,925 Q375,905 375,790 Z" fill="var(--badge-orange)"/>
    <path class="badge-inner" d="M393,264 Q420,262 421,232 Q600,138 779,232 Q780,262 807,264 L807,788 Q807,888 600,906 Q393,888 393,788 Z" fill="url(#badgeFill)" stroke="var(--badge-red)" stroke-width="3"/>

    <text class="brand-title brand-percent" x="600" y="280">100%</text>
    <text class="brand-title brand-word" x="600" y="385">TAURA</text>

    <rect class="bull-artwork" x="465" y="415" width="270" height="320" rx="40" fill="url(#artworkFill)" role="img" aria-label="Bull's head illustration with horns, dark brown"/>

    <path class="ribbon-band" d="M330,700 C470,790 690,800 880,700 L890,790 C700,900 460,890 330,800 Z" fill="url(#ribbonFill)"/>
    <path class="ribbon-edge" d="M336,712 C472,800 690,810 874,712" fill="none" stroke="var(--ribbon-text)" stroke-width="2"/>
    <path class="ribbon-edge" d="M336,792 C462,878 700,888 882,782" fill="none" stroke="var(--ribbon-text)" stroke-width="2"/>

    <text class="ribbon-text ribbon-text-main">
      <textPath href="#ribbonLineOne" startOffset="50%" text-anchor="middle">BEEF PURE</textPath>
    </text>
    <text class="ribbon-text ribbon-text-sub">
      <textPath href="#ribbonLineTwo" startOffset="50%" text-anchor="middle">COOKED AND READY TO EAT</textPath>
    </text>
  </svg>
</main>
</body>
</html>
```